Brit Rock covers band "The Tin Kettles" requires poster for Marlowe Lounge Friday March 31st

I want a design for a poster (A3 and A4) and Facebook/Instagram ads.
Primary focus is the band name logo "The Tin Kettles", style as in attached file, followed by tag "Old Skool Brit Rock".
Backdrop to be 60's psychedelic art.
Secondary focus is the venue "The Marlowe Lounge"
Supporting text to include:
- 27 Fenwick Road, Chatswood SYDNEY
- Friday 31st March 2023
- 7:00 pm until late
- Bar sales refreshments
- NO admission fee

```html
<!DOCTYPE html>
<html lang="en">
<head>
<meta charset="utf-8">
<title>The Tin Kettles – Old Skool Brit Rock</title>
<link rel="stylesheet" href="https://fonts.googleapis.com/css2?family=Oswald:wght@500;700&family=Playfair+Display:wght@700&family=Poppins:wght@600;700&display=swap">
<style>
  :root {
    --stage: #e3e1e2;
    --cream: #fdf0d6;
    --cream-warm: #fde2ad;
    --ray: #fbd58a;
    --ink: #141414;
    --orange: #e8693a;
    --teal: #6aaeaa;
    --pin: #7fb6b2;
    --white: #ffffff;
  }
  * { box-sizing: border-box; margin: 0; padding: 0; }
  html, body { width: 1200px; height: 2561px; overflow: hidden; background: var(--stage); }
  .board {
    position: absolute;
    overflow: hidden;
    box-shadow: 0 6px 18px rgba(0,0,0,.25);
  }
  .board--poster { left: 163px; top: 150px; width: 878px; height: 1241px; }
  .board--square { left: 168px; top: 1543px; width: 870px; height: 869px; }
  .backdrop {
    position: absolute; inset: 0;
    background:
      radial-gradient(ellipse at 50% 45%, rgba(255,250,235,.9) 0%, rgba(255,250,235,0) 55%),
      repeating-linear-gradient(90deg, var(--cream) 0 60px, var(--cream-warm) 60px 90px, var(--ray) 90px 110px, var(--cream) 110px 150px),
      var(--cream);
  }
  .doodles {
    position: absolute; top: 0; bottom: 0; width: 130px;
    background: linear-gradient(180deg, rgba(241,197,60,.35), rgba(203,90,180,.25), rgba(92,160,220,.3), rgba(241,110,70,.35));
  }
  .doodles--left { left: 0; }
  .doodles--right { right: 0; }
  .instruments {
    position: absolute; left: 50%; transform: translateX(-50%); bottom: 0;
    border-radius: 46% 46% 0 0;
    background: linear-gradient(180deg, #c9843a 0%, #8f4f1e 35%, #3a3a3a 65%, #3d7bd0 85%, #e86a4a 100%);
  }
  .content { position: absolute; left: 0; right: 0; text-align: center; }
  .band-name {
    font-family: "Oswald", sans-serif; font-weight: 700; color: var(--ink);
    line-height: .95; letter-spacing: -1px; text-transform: uppercase;
  }
  .tag-top {
    font-family: "Playfair Display", serif; font-weight: 700; color: var(--orange);
    line-height: 1; text-transform: uppercase;
  }
  .tag-main {
    font-family: "Playfair Display", serif; font-weight: 700; color: var(--teal);
    line-height: 1; text-transform: uppercase; letter-spacing: -1px;
  }
  .date-row { display: flex; justify-content: center; align-items: center; }
  .date {
    font-family: "Oswald", sans-serif; font-weight: 500; color: var(--orange);
    line-height: 1; text-transform: uppercase; letter-spacing: -1px;
  }
  .date sup { font-size: .45em; vertical-align: top; position: relative; top: .05em; }
  .year {
    writing-mode: vertical-rl; transform: rotate(180deg);
    font-family: "Poppins", sans-serif; font-weight: 700; color: var(--white);
    background: var(--teal); line-height: 1; padding: 3px 2px;
  }
  .day-time {
    font-family: "Poppins", sans-serif; font-weight: 700; color: var(--orange);
    text-align: left; line-height: 1.05; text-transform: uppercase;
  }
  .venue-pill {
    display: inline-flex; align-items: center; position: relative;
    background: var(--ink); color: var(--white); border-radius: 30px;
    font-family: "Poppins", sans-serif; font-weight: 600; text-transform: uppercase; white-space: nowrap;
  }
  .pin-badge {
    position: absolute; left: -4px; top: 50%; transform: translateY(-50%);
    border-radius: 50%; background: var(--pin); border: 3px solid var(--orange);
    display: flex; align-items: center; justify-content: center;
  }
  .venue-name {
    font-family: "Poppins", sans-serif; font-weight: 700; color: var(--ink);
    line-height: 1; text-transform: uppercase; letter-spacing: 1px;
  }
  .extras {
    font-family: "Poppins", sans-serif; font-weight: 600; color: var(--teal);
    line-height: 1; text-transform: uppercase;
  }
  .extras .dot { color: var(--orange); padding: 0 .5em; }

  /* poster sizes */
  .board--poster .band-name { top: 168px; font-size: 92px; }
  .board--poster .tag-top { top: 388px; font-size: 78px; }
  .board--poster .tag-main { top: 462px; font-size: 104px; }
  .board--poster .date-row { top: 590px; gap: 10px; }
  .board--poster .date { font-size: 86px; }
  .board--poster .year { font-size: 20px; }
  .board--poster .day-time { font-size: 35px; margin-left: 8px; }
  .board--poster .venue-row { top: 682px; }
  .board--poster .venue-pill { height: 42px; font-size: 19px; padding: 0 20px 0 64px; }
  .board--poster .pin-badge { width: 52px; height: 52px; }
  .board--poster .venue-name { top: 742px; font-size: 30px; }
  .board--poster .extras { top: 782px; font-size: 17px; }
  .board--poster .instruments { width: 700px; height: 430px; }

  /* square sizes */
  .board--square .band-name { top: 112px; font-size: 66px; }
  .board--square .tag-top { top: 252px; font-size: 56px; }
  .board--square .tag-main { top: 308px; font-size: 76px; }
  .board--square .date-row { top: 390px; gap: 8px; }
  .board--square .date { font-size: 62px; }
  .board--square .year { font-size: 15px; }
  .board--square .day-time { font-size: 26px; margin-left: 6px; }
  .board--square .venue-row { top: 462px; }
  .board--square .venue-pill { height: 40px; font-size: 19px; padding: 0 18px 0 62px; }
  .board--square .pin-badge { width: 52px; height: 52px; }
  .board--square .venue-name { top: 516px; font-size: 24px; }
  .board--square .extras { top: 548px; font-size: 14px; }
  .board--square .instruments { width: 536px; height: 290px; }
</style>
</head>
<body>

<section class="board board--poster">
  <div class="backdrop" role="img" aria-label="60s psychedelic backdrop of warm cream and amber light rays"></div>
  <div class="doodles doodles--left" role="img" aria-label="colourful line doodles of keyboard, saxophone, leaves and music notes"></div>
  <div class="doodles doodles--right" role="img" aria-label="colourful line doodles of amplifier, guitar, drum and leaves"></div>
  <div class="content band-name">The Tin<br>Kettles</div>
  <div class="content tag-top">Old Skool</div>
  <div class="content tag-main">Brit Rock</div>
  <div class="content date-row">
    <span class="date">31<sup>st</sup> March</span>
    <span class="year">2023</span>
    <span class="day-time">Friday<br>7:00 PM</span>
  </div>
  <div class="content venue-row">
    <span class="venue-pill">
      <span class="pin-badge"><svg width="22" height="26" viewBox="0 0 22 26"><path d="M11 1a8 8 0 0 0-8 8c0 6 8 13 8 13s8-7 8-13a8 8 0 0 0-8-8z" fill="none" stroke="#fff" stroke-width="2"/><circle cx="11" cy="9" r="3" fill="#fff"/><ellipse cx="11" cy="24" rx="7" ry="1.5" fill="none" stroke="#fff" stroke-width="1.5"/></svg></span>
      27 Fenwick Road, Chatswood Sydney
    </span>
  </div>
  <div class="content venue-name">The Marlowe Lounge</div>
  <div class="content extras">Until late<span class="dot">•</span>Bar sales refreshments<span class="dot">•</span>No admission fee</div>
  <div class="instruments" role="img" aria-label="illustrated cluster of instruments: acoustic guitar, saxophone, violin, drum, keyboards, headphones, speakers and records, framed by tropical leaves"></div>
</section>

<section class="board board--square">
  <div class="backdrop" role="img" aria-label="60s psychedelic backdrop of warm cream and amber light rays"></div>
  <div class="doodles doodles--left" role="img" aria-label="colourful line doodles of keyboard, saxophone, leaves and music notes"></div>
  <div class="doodles doodles--right" role="img" aria-label="colourful line doodles of amplifier, guitar, drum and leaves"></div>
  <div class="content band-name">The Tin<br>Kettles</div>
  <div class="content tag-top">Old Skool</div>
  <div class="content tag-main">Brit Rock</div>
  <div class="content date-row">
    <span class="date">31<sup>st</sup> March</span>
    <span class="year">2023</span>
    <span class="day-time">Friday<br>7:00 PM</span>
  </div>
  <div class="content venue-row">
    <span class="venue-pill">
      <span class="pin-badge"><svg width="22" height="26" viewBox="0 0 22 26"><path d="M11 1a8 8 0 0 0-8 8c0 6 8 13 8 13s8-7 8-13a8 8 0 0 0-8-8z" fill="none" stroke="#fff" stroke-width="2"/><circle cx="11" cy="9" r="3" fill="#fff"/><ellipse cx="11" cy="24" rx="7" ry="1.5" fill="none" stroke="#fff" stroke-width="1.5"/></svg></span>
      27 Fenwick Road, Chatswood Sydney
    </span>
  </div>
  <div class="content venue-name">The Marlowe Lounge</div>
  <div class="content extras">Until late<span class="dot">•</span>Bar sales refreshments<span class="dot">•</span>No admission fee</div>
  <div class="instruments" role="img" aria-label="illustrated cluster of instruments: acoustic guitar, saxophone, violin, drum, keyboards, headphones, speakers and records, framed by tropical leaves"></div>
</section>

</body>
</html>
```